Velvet Crest Car Detailing Brochure

I would like a trifold brochure designed for my car detailing business. The background has to be full black or mostly black with some designing using only colors present in our logo.

Front page must have our logo and name, list of services, a photo and mybe our phone number but no long text.

Inside I want to present each service one by one with its description and a photo representing/showing each service. (I will provide the text below). For photos, use stock photos and I will add come of mines already too.

On the back of the brochure I want to have contact & info: phone number, opening hours, address, website, Instagram.

Outside left I want the text About us and photo/design.

I want the brochure to be neat, professional, easy to read, but at the same time not too boring.

Text:
1. About us
a. the ultimate destination for car care in Geneva. We provide personalized, detail-oriented services that bring out the best in your car. With our expert techniques and dedicated approach, we ensure that your car receives the utmost care and attention. Experience a place where passion meets precision and let us create an exceptional car care experience designed just for you.
2. Services:

DETAILING & HAND WASH

• Comprehensive exterior & interior care
• Personalisation and tailored cleaning packages
• Decontamination
• Premium products
• Attention to detail for a perfect finish

POLISHING

• Eliminates scratches, holograms
• Revives and protects paint
• Ensures lasting gloss
• Enhances paint life
• Preserves car’s value and beauty

CERAMIC TREATMENT

• Durable paint protection
• Water-repellent (hydrophobic) effect
• Easier cleaning, enhanced shine
• Long-term surface safeguarding
• Shields against environmental impacts

DRY ICE WASH

• Innovative, waterless method
• Safe for all car parts
• Deep cleans, removes odors
• Allergen-free, antibacterial
• Gentle, effective
• Advanced cleaning technology

COVERING

• Personalized vehicle styling
• More than 150 colours available
• Clean cut without using a cutter
• High-quality, durable materials
• Custom designs available

PROTECTION FILM

• Invisible, durable shield
• Self-healing technology
• 10-year warranty by QR VONT

DETAILING BOUTIQUE

• Premium brands available
• Buy on site during your visit
• Marble Harbour, Zeb Autos, DRUP Polaro
• Essential for at-home car care
• Perfect for quick touch-ups
(for these three brands you can put their logos

Target Market(s)

Our target market includes car owners of all price ranges, with a special focus on those who are passionate about their vehicles. We cater to clients who value excellent service and results, and seek to maintain their cars in pristine condition.

Industry/Entity Type

Automobile / Car detailing

Colors

Designer to choose colors to be used in the design.

Requirements
Must have
• Brand Consistency: The brochure must adhere to our brand colors and style, particularly utilizing the colors present in our logo. Trifold Layout: The design must be specifically tailored for a trifold brochure format. Legibility: Text must be easy to read against the mostly black background, with appropriate font size and style. Professional Look and Feel: The overall design must convey professionalism while being engaging and not overly complex. Photo representation: each service description should have a phot presenting it.
Should not have
• Overcrowded Design: Avoid cluttering with too much text or too many images. The layout should be clean and easy to navigate. Cartoonish Fonts or Graphics: Avoid using unprofessional or casual fonts and graphics that do not align with the upscale and professional image of our business. Distracting Backgrounds: The background should complement and not overpower the content. Stick to the theme of mostly black with design elements from our logo.

```html
<!DOCTYPE html>
<html lang="en">
<head>
<meta charset="utf-8">
<title>Velvet Crest Car Detailing – Trifold Brochure</title>
<link href="https://fonts.googleapis.com/css2?family=Montserrat:wght@400;500;600;700;800&display=swap" rel="stylesheet">
<style>
:root{
  --black:#050507;
  --ink:#0d0d12;
  --pink:#ec2a84;
  --magenta:#c21f8a;
  --purple:#6b3fd4;
  --white:#ffffff;
  --grey:#c9c9d2;
  --paper:#ffffff;
  --panel:264.33px;
}
*{box-sizing:border-box;margin:0;padding:0}
html,body{width:793px;height:1200px;overflow:hidden;background:var(--paper)}
body{font-family:'Montserrat',sans-serif;color:var(--white);position:relative}
.spread{position:absolute;left:0;width:793px;background:var(--black);display:flex;overflow:hidden}
.spread--outside{top:0;height:572px}
.spread--inside{top:594px;height:606px}
.panel{position:relative;width:var(--panel);height:100%;overflow:hidden}
.photo{position:absolute;display:block}
.brand{display:flex;flex-direction:column;align-items:center;gap:8px}
.brand__mark{width:78px;height:78px;border-radius:50%;background:radial-gradient(circle at 35% 30%,#2a1340,#07060c 70%);border:2px solid var(--pink)}
.brand__name{font-weight:700;font-size:13px;letter-spacing:2px;text-transform:uppercase;color:var(--white)}
/* outside left */
.about__photo{left:0;top:0;width:100%;height:168px;background:linear-gradient(160deg,#1b2030 0%,#c8561c 45%,#f08a2a 60%,#2a1b14 100%)}
.about__swoosh{position:absolute;left:0;top:140px}
.about__title{position:absolute;left:22px;top:222px;font-size:22px;font-weight:800;color:var(--pink)}
.about__text{position:absolute;left:22px;top:258px;width:222px;font-size:10.3px;line-height:1.6;color:var(--white)}
/* outside middle */
.contact .brand{position:absolute;top:30px;left:0;width:100%}
.contact__list{position:absolute;left:30px;top:250px;display:flex;flex-direction:column;gap:24px}
.contact__item{display:flex;gap:10px;align-items:flex-start;font-size:10px;line-height:1.5;white-space:nowrap}
.contact__item strong{display:block;font-size:11px;font-weight:700;letter-spacing:.5px}
.contact__row{display:flex;gap:16px}
.contact__row .contact__item{gap:8px;align-items:center}
.contact__row .icon{width:18px;height:18px}
.icon{width:22px;height:22px;flex:none}
.contact__web{position:absolute;bottom:30px;left:0;width:100%;text-align:center;font-size:11px;letter-spacing:3px;color:var(--grey)}
/* outside right */
.cover__curve{position:absolute;left:0;top:0}
.cover .brand{position:absolute;top:18px;left:40px;width:200px}
.services{position:absolute;left:112px;top:126px;list-style:none;font-size:10.5px;font-weight:600;line-height:1.6;white-space:nowrap}
.services li::before{content:"";display:inline-block;width:6px;height:6px;border-radius:50%;background:var(--pink);margin-right:7px;vertical-align:middle}
.cover__photo{left:0;top:262px;width:100%;height:310px;background:radial-gradient(ellipse at 55% 40%,#d9dbe4 0%,#6b6f80 18%,#20222c 45%,#07070a 80%)}
.cover__phone{position:absolute;right:22px;bottom:20px;display:flex;gap:8px;align-items:center;font-size:13px;font-weight:700}
/* inside */
.service{position:absolute;left:0;width:100%;padding:0 16px}
.service__photo{position:relative;width:100%;height:118px;border-radius:2px}
.service__head{display:flex;align-items:center;gap:8px;margin:12px 0 8px}
.service__title{font-size:12px;font-weight:800;letter-spacing:.4px;text-transform:uppercase}
.bullets{list-style:none;font-size:9.6px;line-height:1.6;color:var(--white)}
.bullets li::before{content:"•";color:var(--pink);margin-right:6px}
.divider{position:absolute;top:0;width:1px;height:100%;background:#1d1d25}
.partners{display:flex;gap:8px;margin-top:10px;font-size:7.5px;font-weight:700;letter-spacing:.3px;text-transform:uppercase;white-space:nowrap}
.partners span{padding:4px 0}
.photo--wash{background:linear-gradient(135deg,#2b2f3a,#8a97a8 55%,#1a1d24)}
.photo--polish{background:linear-gradient(135deg,#0e1630,#2f56a8 50%,#0b0f1c)}
.photo--ceramic{background:linear-gradient(135deg,#151a24,#5d6d85 50%,#0a0c12)}
.photo--ice{background:linear-gradient(135deg,#1a1f26,#a9b3bf 50%,#22262d)}
.photo--cover{background:linear-gradient(135deg,#241a2e,#7a6a84 50%,#15121a)}
.photo--film{background:linear-gradient(135deg,#1b1e26,#58606e 50%,#101217)}
</style>
</head>
<body>
<svg width="0" height="0" style="position:absolute">
  <defs>
    <linearGradient id="brandGrad" x1="0" y1="0" x2="1" y2="1">
      <stop offset="0" stop-color="#ec2a84"/><stop offset="1" stop-color="#6b3fd4"/>
    </linearGradient>
    <symbol id="svcIcon" viewBox="0 0 20 20"><rect x="3" y="3" width="14" height="14" rx="3" transform="rotate(45 10 10)" fill="url(#brandGrad)"/></symbol>
  </defs>
</svg>

<!-- OUTSIDE -->
<section class="spread spread--outside">
  <article class="panel about">
    <div class="photo about__photo" role="img" aria-label="Orange sports car parked at night with lights on"></div>
    <svg class="about__swoosh" width="265" height="80" viewBox="0 0 265 80">
      <path d="M0 30 C80 70 170 10 265 40 L265 80 L0 80Z" fill="#050507"/>
      <path d="M0 30 C80 70 170 10 265 40" stroke="url(#brandGrad)" stroke-width="5" fill="none"/>
      <path d="M0 44 C90 78 170 26 265 54" stroke="#6b3fd4" stroke-width="2" fill="none" opacity=".7"/>
    </svg>
    <h2 class="about__title">About Us</h2>
    <p class="about__text">The ultimate destination for car care in Geneva. We provide personalized, detail-oriented services that bring out the best in your car. With our expert techniques and dedicated approach, we ensure that your car receives the utmost care and attention. Experience a place where passion meets precision and let us create an exceptional car care experience designed just for you.</p>
  </article>

  <article class="panel contact">
    <div class="brand"><div class="brand__mark"></div><span class="brand__name">Velvet Crest</span></div>
    <div class="contact__list">
      <div class="contact__item">
        <svg class="icon" viewBox="0 0 24 24"><path d="M12 2a7 7 0 0 0-7 7c0 5 7 13 7 13s7-8 7-13a7 7 0 0 0-7-7zm0 9.5A2.5 2.5 0 1 1 12 6.5a2.5 2.5 0 0 1 0 5z" fill="var(--pink)"/></svg>
        <div><strong>ADDRESS</strong>12, Lorem Ipsum, dolor<br>road, Geneva 1201</div>
      </div>
      <div class="contact__item">
        <svg class="icon" viewBox="0 0 24 24"><circle cx="12" cy="12" r="9" fill="none" stroke="var(--pink)" stroke-width="2.2"/><path d="M12 7v5l3 2" stroke="var(--pink)" stroke-width="2.2" fill="none" stroke-linecap="round"/></svg>
        <div><strong>OPENING HOURS</strong>8:00a.m. to 6:30p.m. daily</div>
      </div>
      <div class="contact__row">
        <div class="contact__item">
          <svg class="icon" viewBox="0 0 24 24"><path d="M6.6 10.8a15 15 0 0 0 6.6 6.6l2.2-2.2a1 1 0 0 1 1-.25 11.4 11.4 0 0 0 3.6.57 1 1 0 0 1 1 1V20a1 1 0 0 1-1 1A17 17 0 0 1 3 4a1 1 0 0 1 1-1h3.5a1 1 0 0 1 1 1 11.4 11.4 0 0 0 .57 3.6 1 1 0 0 1-.25 1z" fill="var(--pink)"/></svg>
          <div>410-555-0182</div>
        </div>
        <div class="contact__item">
          <svg class="icon" viewBox="0 0 24 24"><circle cx="12" cy="12" r="8" fill="var(--pink)"/></svg>
          <div>@velvet_crest</div>
        </div>
      </div>
    </div>
    <p class="contact__web">velvetcrestdetail.com</p>
  </article>

  <article class="panel cover">
    <svg class="cover__curve" width="120" height="270" viewBox="0 0 120 270">
      <path d="M0 40 C70 80 40 180 0 250" stroke="url(#brandGrad)" stroke-width="4" fill="none"/>
      <path d="M0 70 C50 100 30 170 0 220" stroke="#6b3fd4" stroke-width="2" fill="none" opacity=".7"/>
    </svg>
    <div class="brand"><div class="brand__mark"></div><span class="brand__name">Velvet Crest</span></div>
    <ul class="services">
      <li>Detailing &amp; Handwash</li>
      <li>Polishing</li>
      <li>Ceramic Treatment</li>
      <li>Dry Ice Wash</li>
      <li>Covering</li>
      <li>Protection Film</li>
      <li>Detailing Boutique</li>
    </ul>
    <div class="photo cover__photo" role="img" aria-label="Close-up of a car headlight glowing in the dark"></div>
    <div class="cover__phone">
      <svg class="icon" viewBox="0 0 24 24" style="width:16px;height:16px"><path d="M6.6 10.8a15 15 0 0 0 6.6 6.6l2.2-2.2a1 1 0 0 1 1-.25 11.4 11.4 0 0 0 3.6.57 1 1 0 0 1 1 1V20a1 1 0 0 1-1 1A17 17 0 0 1 3 4a1 1 0 0 1 1-1h3.5a1 1 0 0 1 1 1 11.4 11.4 0 0 0 .57 3.6 1 1 0 0 1-.25 1z" fill="var(--pink)"/></svg>
      410-555-0182
    </div>
  </article>
</section>

<!-- INSIDE -->
<section class="spread spread--inside">
  <article class="panel">
    <div class="service" style="top:16px">
      <div class="service__photo photo--wash" role="img" aria-label="Detailer hand washing a car with foam"></div>
      <div class="service__head"><svg class="icon" viewBox="0 0 20 20"><use href="#svcIcon"/></svg><h3 class="service__title">Detailing &amp; Hand Wash</h3></div>
      <ul class="bullets">
        <li>Comprehensive exterior &amp; interior care</li>
        <li>Personalisation and tailored cleaning packages</li>
        <li>Decontamination</li>
        <li>Premium products</li>
        <li>Attention to detail for a perfect finish</li>
      </ul>
    </div>
    <div class="service" style="top:316px">
      <div class="service__photo photo--polish" role="img" aria-label="Polishing machine working on blue car paint"></div>
      <div class="service__head"><svg class="icon" viewBox="0 0 20 20"><use href="#svcIcon"/></svg><h3 class="service__title">Polishing</h3></div>
      <ul class="bullets">
        <li>Eliminates scratches, holograms</li>
        <li>Revives and protects paint</li>
        <li>Ensures lasting gloss</li>
        <li>Enhances paint life</li>
        <li>Preserves car's value and beauty</li>
      </ul>
    </div>
  </article>

  <article class="panel">
    <div class="divider" style="left:0"></div>
    <div class="service" style="top:16px">
      <div class="service__photo photo--ceramic" role="img" aria-label="Ceramic coating applied to a car bonnet"></div>
      <div class="service__head"><svg class="icon" viewBox="0 0 20 20"><use href="#svcIcon"/></svg><h3 class="service__title">Ceramic Treatment</h3></div>
      <ul class="bullets">
        <li>Durable paint protection</li>
        <li>Water-repellent (hydrophobic) effect</li>
        <li>Easier cleaning, enhanced shine</li>
        <li>Long-term surface safeguarding</li>
        <li>Shields against environmental impacts</li>
      </ul>
    </div>
    <div class="service" style="top:316px">
      <div class="service__photo photo--ice" role="img" aria-label="Dry ice blasting cleaning a car engine bay"></div>
      <div class="service__head"><svg class="icon" viewBox="0 0 20 20"><use href="#svcIcon"/></svg><h3 class="service__title">Dry Ice Wash</h3></div>
      <ul class="bullets">
        <li>Innovative, waterless method</li>
        <li>Safe for all car parts</li>
        <li>Deep cleans, removes odors</li>
        <li>Allergen-free, antibacterial</li>
        <li>Gentle, effective</li>
        <li>Advanced cleaning technology</li>
      </ul>
    </div>
  </article>

  <article class="panel">
    <div class="divider" style="left:0"></div>
    <div class="service" style="top:16px">
      <div class="service__photo photo--cover" role="img" aria-label="Installer applying colour wrap vinyl to a car" style="height:96px"></div>
      <div class="service__head"><svg class="icon" viewBox="0 0 20 20"><use href="#svcIcon"/></svg><h3 class="service__title">Covering</h3></div>
      <ul class="bullets">
        <li>Personalized vehicle styling</li>
        <li>More than 150 colours available</li>
        <li>Clean cut without using a cutter</li>
        <li>High-quality, durable materials</li>
        <li>Custom designs available</li>
      </ul>
    </div>
    <div class="service" style="top:272px">
      <div class="service__photo photo--film" role="img" aria-label="Clear protection film being fitted to a car front" style="height:78px"></div>
      <div class="service__head"><svg class="icon" viewBox="0 0 20 20"><use href="#svcIcon"/></svg><h3 class="service__title">Protection Film</h3></div>
      <ul class="bullets">
        <li>Invisible, durable shield</li>
        <li>Self-healing technology</li>
        <li>10-year warranty by QR VONT</li>
      </ul>
      <div class="service__head" style="margin-top:10px"><h3 class="service__title" style="color:var(--pink)">Detailing Boutique</h3></div>
      <ul class="bullets">
        <li>Premium brands available</li>
        <li>Buy on site during your visit</li>
        <li>Marble Harbour, Zeb Autos, DRUP Polaro</li>
        <li>Essential for at-home car care</li>
        <li>Perfect for quick touch-ups</li>
      </ul>
      <div class="partners"><span>Marble Harbour</span><span>Zeb Autos</span><span>DRUP Polaro</span></div>
    </div>
  </article>
</section>
</body>
</html>
```